Seminar Flyer

We would like a flyer describing a seminar we will be presenting to window cleaners. The seminar topic is Glass Restoration and will include discussions on types of glass, types of glass damage and solutions. I am including the following (sample) description:
"Spend a day with The PaneMaven and learn how you can benefit from learning "Glass Restoration" and the many benefits to offering this service to your clients.
Before investing a lot of "time and money" in ANY Glass Restoration System, learn what Glass Restoration is all about and how you can turn a small investment into a very profitable business. And, this new business can be easily expanded into several other related business's.
Ready to expand your business and make some great money?
"DON'T WAIT" - Start offering your clients Glass Restoration Services.
"Glass Restoration" is one of the most profitable "Add-On" businesses for the window cleaning industry and you now have an opportunity to learn from one of the industry
leaders. Lyle Brandt will be offering a full day "hands-on" seminar on Glass Restoration.
The seminar will cover:
Glass Types
Glass Damage
Glass Coatings
Glass Distortion & Breakage
Glass Restoration Systems
Glass Restoration Procedures
Customer Expectations
Marketing and Pricing a job
Hands on demonstrations
And much much more.....
And did I mention it will cover "Glass"?
This full day seminar will be presented by Lyle Brandt and sponsored by the H.Morwick Company at their facility in Carson, California.
Space will be limited, so you must register to attend, but the seminar and lunch is FREE.
This all day seminar will also cover discussions on:
Hard Water Spot Removal and methods for removing.
What exactly is "Tin Etch Haze" and how to prevent or remove it easily.
Minor scratch removal (light scratches and metal marks)
Tempered Glass Defects - Waivers and precautions
Excess Scratch removal (tempered Glass scratching)
Graffiti Removal (major scratch and acid etch damage)
Additional Money Makers:
Anti-Graffiti Film Application
- An easy add on business for glass restoration businesses
Hard Water Spot Removal and Glass Sealant
- An easy add on business for window cleaning businesses
Window Frame Restoration and Treatment
- An easy add on business for window cleaning businesses"
Lyle Brandt, the President of The Brandt Company, is well known in the window cleaning industry as "PaneMaven", so we want to make sure that branding is included in the flyer.
PLEASE NOTE: The flyer will be distributed as an e-mail attachment so the flyer itself will not have any specific information regarding dates and location.
Target Market(s)
Window Cleaners; small business owners.
Industry/Entity Type
Window Cleaning

```html
<!DOCTYPE html>
<html lang="en">
<head>
<meta charset="utf-8">
<title>Glass Restoration Seminar</title>
<link rel="stylesheet" href="https://fonts.googleapis.com/css2?family=Arimo:wght@400;700&family=Mulish:wght@300;400&display=swap">
<style>
:root{
  --bg:#393a3b;
  --accent:#2ba8da;
  --ink:#ffffff;
  --frame:#8fd3ee;
}
*{margin:0;padding:0;box-sizing:border-box}
html,body{width:849px;height:1200px;overflow:hidden;background:var(--bg)}
.flyer{position:relative;width:849px;height:1200px;background:var(--bg);color:var(--ink);font-family:"Arimo",Arial,sans-serif}
.brand{position:absolute;left:42px;top:30px;display:flex;align-items:center;gap:22px}
.brand-mark{width:30px;height:96px;background:var(--accent)}
.brand-name{font-family:"Mulish",sans-serif;font-weight:300;font-size:27px;letter-spacing:4px;line-height:41px;color:var(--ink)}
.title{position:absolute;left:420px;top:126px;font-family:"Mulish",sans-serif;font-weight:300;font-size:41px;letter-spacing:1px;color:var(--accent);line-height:1}
.intro{position:absolute;left:54px;top:250px;width:743px;font-size:14.6px;line-height:19.4px;text-align:justify}
.intro p{margin-bottom:19.4px}
.hl{color:var(--accent)}
.cover{position:absolute;left:54px;top:530px;width:743px;font-size:14.6px;line-height:19.6px}
.section-head{color:var(--accent);font-size:15.4px;line-height:20px}
.cover-list{display:grid;grid-template-columns:356px 1fr;list-style:none}
.presenter{position:absolute;left:54px;top:691px;width:743px;font-size:14.6px;line-height:19.4px;text-align:justify}
.notice{position:absolute;left:0;top:751px;width:849px;text-align:center;color:var(--accent);font-size:15.2px}
.discussions{position:absolute;left:54px;top:795px;width:410px;font-size:14.6px;line-height:19.2px}
.money{position:absolute;left:478px;top:795px;width:320px;font-size:14.6px;line-height:19.2px}
.discussions .section-head,.money .section-head{margin-bottom:9px}
.plain-list{list-style:none}
.money .note{font-style:italic;padding-left:16px;text-indent:-16px}
.photo{position:absolute;top:1041px;height:131px;border:3px solid var(--frame);border-radius:6px}
.photo-1{left:93px;width:211px;background:linear-gradient(135deg,#6f7a78,#c9cfcc 55%,#5d6663)}
.photo-2{left:337px;width:175px;background:linear-gradient(135deg,#5b6360,#bfc5c2 50%,#7d8580)}
.photo-3{left:580px;width:191px;background:linear-gradient(135deg,#4a4f55,#8c8470 50%,#2f3438)}
</style>
</head>
<body>
<main class="flyer">
  <header class="brand">
    <span class="brand-mark"></span>
    <span class="brand-name">Pane<br>Maven</span>
  </header>
  <h1 class="title">Glass Restoration</h1>

  <section class="intro">
    <p>Spend a day with The <span class="hl">PaneMaven</span> and learn how you can benefit from learning "<span class="hl">Glass Restoration</span>" and the many benefits to offering this service to your clients.</p>
    <p>Before investing a lot of "<span class="hl">time and money</span>" in ANY Glass Restoration System, learn what Glass Restoration is all about and how you can turn a small investment into a very profitable business. And, this new business can be easily expanded into several other related business's.</p>
    <p>Ready to expand your business and make some great money?<br>"<span class="hl">DON'T WAIT</span>" - Start offering your clients Glass Restoration Services.</p>
    <p>"<span class="hl">Glass Restoration</span>" is one of the most profitable "<span class="hl">Add-On</span>" businesses for the window cleaning industry and you now have an opportunity to learn from one of the industry leaders. Lyle Brandt will be offering a full day "hands-on" seminar on Glass Restoration.</p>
  </section>

  <section class="cover">
    <h2 class="section-head">The seminar will cover:</h2>
    <ul class="cover-list">
      <li>Glass Types</li><li>Glass Damage</li>
      <li>Glass Coatings</li><li>Glass Distortion &amp; Breakage</li>
      <li>Glass Restoration Systems</li><li>Glass Restoration Procedures</li>
      <li>Customer Expectations</li><li>Marketing and Pricing a job</li>
      <li>Hands on demonstrations</li><li>And much much more.....</li>
      <li>And did I mention it will cover "<span class="hl">Glass</span>"?</li>
    </ul>
  </section>

  <p class="presenter">This full day seminar will be presented by <span class="hl">Lyle Brandt</span> and sponsored by the <span class="hl">H.Morwick Company</span> at their facility in Carson, California.</p>

  <p class="notice">Space will be limited, so you must register to attend, but the seminar and lunch is FREE.</p>

  <section class="discussions">
    <h2 class="section-head">This all day seminar will also cover discussions on:</h2>
    <ul class="plain-list">
      <li>Hard Water Spot Removal and methods for removing.</li>
      <li>What exactly is "Tin Etch Haze" and how to prevent or remove it easily.</li>
      <li>Minor scratch removal (light scratches and metal marks)</li>
      <li>Tempered Glass Defects - Waivers and precautions</li>
      <li>Excess Scratch removal (tempered Glass scratching)</li>
      <li>Graffiti Removal (major scratch and acid etch damage)</li>
    </ul>
  </section>

  <section class="money">
    <h2 class="section-head">Additional Money Makers:</h2>
    <ul class="plain-list">
      <li>Anti-Graffiti Film Application</li>
      <li class="note">-&nbsp;&nbsp;An easy add on business for glass restoration businesses</li>
      <li>Hard Water Spot Removal and Glass Sealant</li>
      <li class="note">-&nbsp;&nbsp;An easy add on business for window cleaning businesses</li>
      <li>Window Frame Restoration and Treatment</li>
      <li class="note">-&nbsp;&nbsp;An easy add on business for window cleaning businesses</li>
    </ul>
  </section>

  <div class="photo photo-1" role="img" aria-label="Shop window glass covered in scratched graffiti tags"></div>
  <div class="photo photo-2" role="img" aria-label="Glass pane with heavy etched graffiti damage"></div>
  <div class="photo photo-3" role="img" aria-label="Storefront window after glass restoration"></div>
</main>
</body>
</html>
```